Tallowin geriatric care need letterhead design

Please help to design a letterhead document which will will be used as correspondent letter to other doctors.

apart from designing the letterhead, please also do the arrangement for the format so that it can be ready to use.

Please allocate page number at the bottom of the letter and also, small print for Tallowin geriatric care on the bottom of the page.
the template will need to be workable on word document so that the letter can be typed out with perfect match.

Format :
17th July 2104
To: Dr.xxx
Address.........

Re: Mr. NNN
Address
DOB

Dear Dr XXX,

Kind regards,

Dr. SSS
Provider no. 8592043

I do not have a physical address, tel or fax currently so, please allocated specific area for the company detail.

There will be up to 3 address on the letter with one of it been the main address

Eg.
Main Room--address
other consultation address

Thank you

Dear all designers, Please help to design the letter head. don't worry about the previous brief. use your imagination and no need to worry about the patient detail etc. The following information need to be in the letterhead Main room Suite 6.14 Norvu Medical 241-243 Corbel Street Carrow Hill VIC 3281 Phone: Fax: Peripheral room: Kelvindale Medical Centre street, mooroolbark VIC 3333 Our Lady of Pemberly, 4718 dunmarra road, franskton vic 3199 Quenton Private specialist clinic, 867 pelliton road, mt. waverley vic 3333 please put in the ABN: 690371 which is the company registration no. ( in a small font as it doesn't need to bed obvious) somewhere on the top.

```html
<!DOCTYPE html>
<html lang="en">
<head>
<meta charset="utf-8">
<title>Tallowin Geriatric Care – Letterhead</title>
<link href="https://fonts.googleapis.com/css2?family=Open+Sans:wght@400;600&display=swap" rel="stylesheet">
<style>
  :root {
    --backdrop: #e6e6e6;
    --paper: #ffffff;
    --navy: #1f2a5e;
    --red: #c41e2c;
    --grey: #8a8a8a;
    --watermark: #ededed;
  }
  * { box-sizing: border-box; margin: 0; padding: 0; }
  html, body { width: 1200px; height: 968px; overflow: hidden; }
  body {
    background: var(--backdrop);
    font-family: "Open Sans", Arial, sans-serif;
    color: var(--navy);
    position: relative;
  }
  .letterhead {
    position: absolute;
    left: 275px; top: 24px;
    width: 650px; height: 920px;
    background: var(--paper);
    box-shadow: 0 2px 10px rgba(0,0,0,0.12);
    overflow: hidden;
  }
  .brand {
    position: absolute;
    right: 44px; top: 44px;
    display: flex; align-items: center; gap: 10px;
  }
  .brand-dot {
    width: 14px; height: 14px; border-radius: 50%;
    background: var(--red); display: inline-block;
  }
  .brand-name {
    font-size: 22px; font-weight: 600;
    color: var(--red);
  }
  .abn {
    position: absolute; right: 44px; top: 118px;
    font-size: 9px; color: var(--navy);
  }
  .watermark {
    position: absolute; right: -80px; top: 140px;
    width: 260px; height: 260px; border-radius: 50%;
    background: var(--watermark);
  }
  .locations {
    position: absolute; left: 44px; bottom: 130px; right: 30px;
    display: flex; align-items: flex-start;
    font-size: 9px; line-height: 1.4;
  }
  .location {
    font-style: normal;
    padding: 0 18px 18px 12px;
  }
  .location:first-child { padding-left: 0; }
  .location + .location { border-left: 1.5px solid var(--red); }
  .location-label { color: var(--red); }
  .contact-key { color: var(--red); }
  .signoff {
    position: absolute; left: 150px; bottom: 62px;
    line-height: 1.35;
  }
  .website { font-size: 11px; color: var(--red); }
  .signoff-name { font-size: 13px; color: var(--navy); }
</style>
</head>
<body>
  <main class="letterhead">
    <header class="brand">
      <span class="brand-dot"></span>
      <span class="brand-name">Tallowin Geriatric Care</span>
    </header>
    <p class="abn">ABN: 47 690 371 208</p>
    <div class="watermark" role="img" aria-label="Faint brand decoration"></div>

    <footer>
      <div class="locations">
        <address class="location">
          <span class="location-label">Main room</span><br>
          Suite 6.14<br>
          Norvu Medical centre<br>
          241-243 Corbel Street<br>
          Carrow Hill VIC 3281<br>
          <span class="contact-key">P:</span> (03) 9417 2208<br>
          <span class="contact-key">F:</span> (03) 8630 5914
        </address>
        <address class="location">
          Kelvindale Medical Centre,<br>
          52 Linford Rd,<br>
          Kelvindale VIC 3395
        </address>
        <address class="location">
          Quenton Private specialist clinic,<br>
          867 Pelliton Rd,<br>
          Mt. Quenton VIC 3407
        </address>
        <address class="location">
          Our Lady of Pemberly,<br>
          4718 Dunmarra Rd,<br>
          Pemberly VIC 3512
        </address>
      </div>
      <div class="signoff">
        <div class="website">www.tallowingc.com.au</div>
        <div class="signoff-name">Tallowin Geriatric Care</div>
      </div>
    </footer>
  </main>
</body>
</html>
```